Design Contest For Business Cards and PostCards (over-sized/standard)

Type of Contest : Business Card and PostCard Design

Size Requirements : Not 100% sure, whatever size looks best for both business cards and the postcards.

Color Requirements : Include colors from the Logo provided

General Requirements : I will need the template and the formats of both the business card and the postcard at the time of completion and upon receiving payment. Must include logo provided.

Additional Information : I'm a personal trainer that provides fitness instruction and helps clients achieve their goals through exercise and nutrition. Information is below
Business Card:
Company: ORA BOLD WELLNESS
Personal Training|Bootcamp|Kickboxing|Nutrition
Name: Dorian Kettleby
Website: OraBoldWellness.com
Phone: 555.014.2297
Addtl: Somewhere it should say, "Schedule your free session or assessment today" and a quote that says, “Motivation is what gets you started. Habit is what keeps you going.” or "Bold your Fitness"

PostCard (for mailing to potential customers' households)
Company: ORA BOLD WELLNESS
Name: Dorian Kettleby
Phone: 555.014.2297
**Try a free week of Ora Bold Bootcamp**

***The rest of the creativity is up to the designer and i'm looking for double sided on both. I will be using the winning design to upload to either a stampleo or something like it. Thank you.

```html
<!DOCTYPE html>
<html lang="en">
<head>
<meta charset="utf-8">
<title>Ora Bold Wellness — Business Card</title>
<link rel="stylesheet" href="https://fonts.googleapis.com/css2?family=Open+Sans:wght@400;600;700;800&display=swap">
<style>
  :root {
    --page: #e8e5e0;
    --card-white: #ffffff;
    --card-mist: #e2e3e7;
    --brand-blue: #1d5c9e;
    --brand-ink: #1f2229;
    --text-blue: #2a64a8;
    --soft-shape: #eef0f4;
  }
  * { margin: 0; padding: 0; box-sizing: border-box; }
  html, body {
    width: 1200px; height: 900px; overflow: hidden;
    background: var(--page);
    font-family: "Open Sans", Arial, sans-serif;
  }
  .sheet {
    width: 1200px; height: 900px;
    display: flex; flex-direction: column; align-items: center;
    justify-content: center; gap: 48px;
  }
  .card {
    position: relative; width: 640px; height: 366px; overflow: hidden;
    box-shadow: 0 6px 18px rgba(0,0,0,.18);
  }

  .brand-mark {
    position: absolute; display: flex; align-items: center; gap: 14px;
    color: var(--brand-ink); font-weight: 800; letter-spacing: .5px; white-space: nowrap;
  }
  .brand-dot { flex: none; border-radius: 50%; background: var(--brand-blue); }

  /* Front */
  .card--front {
    background: radial-gradient(ellipse at 50% 35%, var(--card-white) 0%, var(--card-mist) 100%);
  }
  .card--front .brand-mark { left: 50%; top: 112px; transform: translateX(-50%); font-size: 38px; }
  .card--front .brand-dot { width: 30px; height: 30px; }
  .front-band { position: absolute; left: 0; right: 0; background: var(--brand-blue); }
  .front-band--wide { top: 258px; height: 28px; }
  .front-band--thin { top: 318px; height: 16px; }

  /* Back */
  .card--back { background: var(--card-white); }
  .soft-shape { position: absolute; right: 0; top: 0; width: 380px; height: 366px; }
  .card--back .brand-mark { right: 44px; top: 66px; font-size: 24px; }
  .card--back .brand-dot { width: 20px; height: 20px; }
  .trainer-name {
    position: absolute; left: 40px; top: 126px;
    color: var(--text-blue); font-size: 22px; font-weight: 700;
  }
  .services {
    position: absolute; left: 58px; top: 166px;
    color: var(--text-blue); font-size: 13px; font-weight: 600; line-height: 20px;
  }
  .phone {
    position: absolute; left: 40px; top: 290px;
    color: var(--text-blue); font-size: 14px; font-weight: 600;
  }
  .promo-band {
    position: absolute; left: 250px; right: 0; top: 184px; height: 130px;
    background: var(--brand-blue); color: var(--card-white);
    clip-path: polygon(40px 0, 100% 0, 100% 100%, 0 100%);
    display: flex; flex-direction: column; justify-content: center; align-items: center;
    padding-left: 40px; text-align: center; gap: 6px;
  }
  .promo-band .slogan { font-size: 24px; font-weight: 700; }
  .promo-band .offer { font-size: 13px; font-weight: 700; }
</style>
</head>
<body>
<main class="sheet">
  <section class="card card--front" aria-label="Business card front">
    <div class="brand-mark"><span class="brand-dot"></span>ORA BOLD WELLNESS</div>
    <div class="front-band front-band--wide"></div>
    <div class="front-band front-band--thin"></div>
  </section>

  <section class="card card--back" aria-label="Business card back">
    <svg class="soft-shape" viewBox="0 0 380 366" aria-hidden="true">
      <path d="M60 366 C90 200 200 70 380 10 L380 366 Z" fill="var(--soft-shape)"/>
    </svg>
    <div class="brand-mark"><span class="brand-dot"></span>ORA BOLD WELLNESS</div>
    <h1 class="trainer-name">Dorian Kettleby</h1>
    <ul class="services">
      <li>Personal Training</li>
      <li>Bootcamp</li>
      <li>Kickboxing</li>
      <li>Nutrition</li>
    </ul>
    <p class="phone">Phone: 555.014.2297</p>
    <div class="promo-band">
      <p class="slogan">"Bold your Fitness"</p>
      <p class="offer">"Schedule your free session or assessment today"</p>
    </div>
  </section>
</main>
</body>
</html>
```